Re-design existing website and add products for sale.

Our current website is very basic and cluttered. (brightwillowcare.com.au)We want a modern looking website that is easy to navigate. We also want to start selling essential oils and crystal products, so there needs to be a separate page for this. Also needs to be easily edited as we need to change the monthly oracle card with the description. Would like calming colours as we are all about natural healing. Alongside the services listed there should be a button to book now which asks for their name, email, phone number ect. and adds it to the cart.

• Logo is still being designed, please leave a space for the logo which will basically be a lotus flower within a mandala.

```html
<!DOCTYPE html>
<html lang="en">
<head>
<meta charset="utf-8">
<title>Bright Willow Care</title>
<link href="https://fonts.googleapis.com/css2?family=Nunito:wght@700;800;900&family=Open+Sans:wght@400;600;700&display=swap" rel="stylesheet">
<style>
:root{
  --blue:#1aa2dc;
  --blue-dark:#0f8fc6;
  --violet:#b27fd0;
  --pink:#f3c6dc;
  --dark:#2a2226;
  --night:#120d10;
  --white:#ffffff;
  --ink:#333333;
}
*{margin:0;padding:0;box-sizing:border-box}
html,body{width:803px;height:1200px;overflow:hidden}
body{position:relative;font-family:"Open Sans",sans-serif;color:var(--ink);background:var(--white)}
.abs{position:absolute}
.topbar{left:0;top:0;width:803px;height:26px;background:linear-gradient(90deg,#9b86b0,#c8b0c8 50%,#9b86b0)}
.topbar .phone{left:170px;top:6px;font-size:7px;font-weight:600;color:var(--white);display:flex;align-items:center;gap:6px}
.social{top:5px;display:flex;gap:8px;left:598px}
.social span{width:16px;height:16px;border:1.5px solid var(--white);border-radius:50%;display:block}
.nav{left:0;top:26px;width:803px;height:24px;background:var(--blue)}
.nav a{position:absolute;top:6px;font-size:8px;font-weight:600;color:var(--white);text-decoration:none}
.hero{left:0;top:50px;width:803px;height:228px;background:radial-gradient(circle at 400px 60px,#fff4f8 0,#d8b9d8 12%,#8f7ea8 35%,#5e5479 70%,#3b3550 100%)}
.hero-scene{left:0;top:50px;width:803px;height:228px;background:linear-gradient(180deg,transparent 55%,rgba(40,35,60,.55) 80%,#14111a 100%)}
.figure{left:418px;top:70px;width:80px;height:160px;background:linear-gradient(180deg,#3a2f45,#1d1724);border-radius:30px 30px 10px 10px;opacity:.85}
.hero-title{left:166px;top:108px;font-family:"Nunito",sans-serif;font-weight:800;font-size:16px;line-height:20px;color:var(--white)}
.hero-sub{left:166px;top:149px;font-size:11px;color:var(--white)}
.btn{background:var(--blue);color:var(--white);font-size:7px;text-align:center;border-radius:3px}
.hero .btn{}
.dots{left:375px;top:268px;width:54px;height:10px;background:var(--white);border-radius:3px 3px 0 0;display:flex;justify-content:center;gap:6px;align-items:center}
.dots i{width:5px;height:5px;border:1px solid #666;border-radius:50%;display:block}
.dots i.on{border-color:#e0407a}
.logo-diamond{left:366px;top:14px;width:70px;height:70px;background:var(--white);transform:rotate(45deg);box-shadow:0 2px 4px rgba(0,0,0,.25)}
.logo-text{left:366px;top:36px;width:70px;text-align:center;font-family:"Nunito",sans-serif;font-weight:700;font-size:8px;line-height:10px;color:#222}
.logo-dot{left:393px;top:26px;width:16px;height:9px;border-radius:50%;background:var(--violet)}
.why{left:0;top:278px;width:803px;height:156px;background:var(--blue);color:var(--white);text-align:center}
.why h2{font-family:"Nunito",sans-serif;font-weight:900;font-size:16px;margin-top:16px}
.why p{font-size:6.3px;line-height:8px;width:420px;margin:8px auto 0}
.services{left:0;top:434px;width:803px;height:281px;background:var(--white);overflow:hidden}
.deco-l{left:-10px;top:20px;width:180px;height:180px;background:radial-gradient(ellipse,rgba(243,198,220,.35),transparent 70%)}
.deco-r{left:620px;top:70px;width:200px;height:180px;background:radial-gradient(ellipse,rgba(243,198,220,.35),transparent 70%)}
.services h2{left:0;width:803px;top:17px;text-align:center;font-family:"Nunito",sans-serif;font-weight:900;font-size:16px;color:var(--blue)}
.services .lead{left:0;width:803px;top:36px;text-align:center;font-size:6px}
.svc{top:70px;width:140px;text-align:center;font-size:6.5px;line-height:8px}
.svc .photo{width:125px;height:125px;border-radius:50%;margin:0 auto 10px}
.svc b{color:var(--blue);font-weight:600;display:block}
.believe{left:0;top:715px;width:803px;height:248px;background:radial-gradient(circle at 400px 100px,#4a3a40,var(--dark) 60%,#1f181b)}
.lotus-art{left:0;top:15px;width:245px;height:233px;background:radial-gradient(ellipse at 50% 80%,#c36fe0 0,#8c55b8 40%,rgba(90,60,120,.4) 70%,transparent 75%)}
.believe h2{left:200px;width:403px;top:16px;text-align:center;font-family:"Nunito",sans-serif;font-weight:900;font-size:16px;line-height:20px;color:var(--blue)}
.believe p{left:252px;width:300px;top:64px;text-align:center;font-size:6.3px;line-height:8px;color:var(--white)}
.believe p a{color:var(--blue);font-weight:700;text-decoration:none}
.benefits{left:252px;top:120px;list-style:none;color:var(--white);font-size:6.5px;font-weight:700}
.benefits li{height:12px;display:flex;align-items:center;gap:5px}
.benefits li::before{content:"";width:10px;height:4px;border-radius:50%;background:var(--violet)}
.frame{border:2.5px solid var(--blue)}
.room1{left:424px;top:116px;width:113px;height:113px;background:linear-gradient(160deg,#3a3f6a,#6a4b2c 55%,#7a2a3a)}
.room2{left:536px;top:92px;width:116px;height:116px;background:linear-gradient(160deg,#f2f2f2,#9a9a9a 60%,#3a3a3a)}
.contact{left:0;top:963px;width:803px;height:217px;background:radial-gradient(circle at 330px 80px,#3a2a2c,var(--night) 65%)}
.contact h3{font-family:"Nunito",sans-serif;font-weight:800;font-size:17px;color:var(--white);position:absolute;top:18px}
.item{left:166px;display:flex;gap:8px;color:var(--white);font-size:6.5px;line-height:8px}
.item b{font-size:7.5px;display:block}
.form input,.form textarea{position:absolute;background:transparent;border:1.5px solid var(--white);border-radius:3px;color:var(--white);font:6.5px "Open Sans",sans-serif;padding:0 4px}
.form input::placeholder,.form textarea::placeholder{color:#ddd}
.form textarea{padding-top:4px;resize:none}
.submit{left:481px;top:189px;width:73px;height:15px;line-height:15px;background:var(--white);color:var(--blue);font-size:6.5px;text-align:center;border-radius:3px}
.footer{left:0;top:1180px;width:803px;height:20px;background:var(--white)}
.footer small{position:absolute;left:166px;top:5px;font-size:6.5px}
.foot-logo{left:376px;top:1157px;width:52px;height:43px;background:var(--white);text-align:center;font-family:"Nunito",sans-serif;font-weight:700;font-size:6.5px;line-height:8px;color:#222;padding-top:20px}
.foot-logo::before{content:"";position:absolute;left:19px;top:7px;width:14px;height:8px;border-radius:50%;background:var(--violet)}
</style>
</head>
<body>

<div class="abs topbar">
  <div class="abs phone">
    <svg width="12" height="12" viewBox="0 0 24 24" fill="none" stroke="#fff" stroke-width="2"><path d="M5 3h4l2 5-3 2a11 11 0 0 0 6 6l2-3 5 2v4a2 2 0 0 1-2 2A18 18 0 0 1 3 5a2 2 0 0 1 2-2z"/></svg>
    0400-218-775
  </div>
  <div class="abs social"><span></span><span></span></div>
</div>

<nav class="abs nav">
  <a style="left:214px" href="#">HOME</a>
  <a style="left:254px" href="#">About</a>
  <a style="left:294px" href="#">Products</a>
  <a style="left:474px" href="#">Book</a>
  <a style="left:510px" href="#">Courses</a>
  <a style="left:557px" href="#">Contact Us</a>
</nav>

<section>
  <div class="abs hero" role="img" aria-label="Silhouette of a woman in tree pose against a misty mountain sunrise"></div>
  <div class="abs hero-scene"></div>
  <div class="abs figure"></div>
  <h1 class="abs hero-title">Find Your True Self and<br>Bring Balance to Your Life</h1>
  <div class="abs hero-sub">Living a Healthy Happy Life</div>
  <div class="abs btn" style="left:166px;top:173px;width:74px;height:15px;line-height:15px">Learn More</div>
  <div class="abs dots"><i></i><i class="on"></i><i></i><i></i></div>
</section>

<div class="abs logo-diamond"></div>
<div class="abs logo-dot"></div>
<div class="abs logo-text">Bright Willow<br>Care</div>

<section class="abs why">
  <h2>WHY CHOOSE US</h2>
  <p>Are you struggling through life, feeling stuck, not feeling yourself, or simply feeling drained? Need to find a way to relax and rejuvenate, a way to free up your energy to work on that which better serves you in this lifetime?</p>
  <p>Working together with you, I can help you achieve this. Whether through spiritual healing sessions using Reiki and Seichim, through Oracle Card Readings or a combination of these.</p>
  <p>I am passionate about using my knowledge and skills to help others struggling through their life journey.</p>
  <p>Reiki and Seichim workshops are also available for those who wish to learn Reiki or Seichim for themselves.</p>
  <p>Furthermore, 10% of proceeds from all services are donated to a different charity each month in order to help those who are less fortunate.</p>
</section>

<section class="abs services">
  <div class="abs deco-l" role="img" aria-label="Faint pink lotus line drawing"></div>
  <div class="abs deco-r" role="img" aria-label="Faint pink lotus line drawing"></div>
  <h2 class="abs">SERVICES</h2>
  <div class="abs lead">Some of the services on offer include</div>
  <div class="abs svc" style="left:158px">
    <div class="photo" role="img" aria-label="Pink meditation illustration with glowing figure" style="background:radial-gradient(circle,#f7c6ec,#d46ac0 55%,#8a2f86)"></div>
    <b>Reiki/Seichim Healings</b>1 Hour - $75<br>1/2 Hour - $40
  </div>
  <div class="abs svc" style="left:331px">
    <div class="photo" role="img" aria-label="Portrait photo of a Reiki teacher in orange robes" style="background:radial-gradient(circle at 50% 70%,#d9731e,#6b4a2e 55%,#3b3a34)"></div>
    <b>Reiki/Seichim Workshops</b>Reiki 1 Workshop - $180<br>Reiki 2 Workshop - $280
  </div>
  <div class="abs svc" style="left:503px">
    <div class="photo" role="img" aria-label="Oracle card illustration in lilac tones" style="background:radial-gradient(circle,#eadcf0,#b593cf 55%,#6b4a8e)"></div>
    <b>Reiki/Seichim Healings</b>1 Hour - $75<br>1/2 Hour - $40
  </div>
  <div class="abs btn" style="left:365px;top:246px;width:73px;height:15px;line-height:15px">View More</div>
</section>

<section class="abs believe">
  <div class="abs lotus-art" role="img" aria-label="Purple lotus flower with a seated meditation silhouette"></div>
  <h2 class="abs">We believe that it is a basic human right<br>to feel good in your body</h2>
  <p class="abs">You deserve to feel good. You are worthy of feeling good. At Bright Willow Care, we are here to help you on your journey to optimal health and wellbeing. Our <a href="#">Services</a> play an integral role in taking care of your body. <a href="#">Contact us</a> if you are looking to:</p>
  <ul class="abs benefits">
    <li>Decrease pain</li>
    <li>Balance hormones</li>
    <li>Manage stress and tension</li>
    <li>Restore energy</li>
    <li>Increase mindfulness and awareness</li>
  </ul>
  <div class="abs frame" style="left:422px;top:140px;width:40px;height:91px;border-right:none;border-top:none"></div>
  <div class="abs frame" style="left:533px;top:89px;width:119px;height:66px;border-bottom:none;border-left:none"></div>
  <div class="abs frame" style="left:533px;top:89px;width:40px;height:20px;border-right:none;border-bottom:none"></div>
  <div class="abs frame" style="left:612px;top:176px;width:40px;height:35px;border-left:none;border-top:none"></div>
  <div class="abs room1" role="img" aria-label="Singing bowls on a colourful woven cloth"></div>
  <div class="abs room2" role="img" aria-label="Treatment room with healing bed and wall art"></div>
</section>

<section class="abs contact">
  <h3 style="left:166px">CONTACT:</h3>
  <div class="abs item" style="top:52px">
    <svg width="14" height="14" viewBox="0 0 24 24" fill="none" stroke="#fff" stroke-width="1.6"><path d="M12 22s7-7 7-12a7 7 0 0 0-14 0c0 5 7 12 7 12z"/><circle cx="12" cy="10" r="2.5"/></svg>
    <div><b>Bright Willow Care.</b>14 Marlow Lane<br>Seacliff, SA 5049</div>
  </div>
  <div class="abs item" style="top:100px">
    <svg width="14" height="12" viewBox="0 0 24 18" fill="none" stroke="#fff" stroke-width="1.6"><rect x="1" y="1" width="22" height="16"/><path d="M1 1l11 9 11-9"/></svg>
    <div><b>Email</b>hello@brightwillowcare.com.au</div>
  </div>
  <div class="abs item" style="top:136px">
    <svg width="14" height="14" viewBox="0 0 24 24" fill="none" stroke="#fff" stroke-width="1.6"><path d="M5 3h4l2 5-3 2a11 11 0 0 0 6 6l2-3 5 2v4a2 2 0 0 1-2 2A18 18 0 0 1 3 5a2 2 0 0 1 2-2z"/></svg>
    <div><b>Telephone</b>0400-218-775</div>
  </div>
  <h3 style="left:479px">GET IN TOUCH</h3>
  <form class="form">
    <input style="left:480px;top:52px;width:74px;height:15px" placeholder="First Name *">
    <input style="left:562px;top:52px;width:74px;height:15px" placeholder="Last Name *">
    <input style="left:480px;top:76px;width:156px;height:15px" placeholder="Email *">
    <input style="left:480px;top:100px;width:156px;height:15px" placeholder="Subject">
    <textarea style="left:480px;top:124px;width:156px;height:56px" placeholder="Message"></textarea>
    <div class="abs submit">SUBMIT</div>
  </form>
</section>

<footer class="abs footer"><small>© 2019 All Right Reserved.</small></footer>
<div class="abs foot-logo">Bright Willow<br>Care</div>

</body>
</html>
```